Design material for Lumora Summit

We need a design of POSM for Lumora Summit
1. Content:
- The Lumora Summit 3rd
- Singapore 28.10.2018
- A placeholder for insert logo of sponsors (limit 10 logo)
2. POSM:
- Backdrop: 5,5m and 2,6m
- Banner: 4m and 0,5m
- Standee: 0,8m and 2m
- Cover: A4 size
3. Style:
We need style simply because we are a hospital.
Main color: light blue and a little of green (if can)

Hope to see your design soon!

Font styles to use
Sans Serif

Colors
0792cd
85cae6
86cfc6
33b8a4
33a6d7

```html
<!DOCTYPE html>
<html lang="en">
<head>
<meta charset="utf-8">
<title>Lumora Summit 2018 – Cover</title>
<link rel="stylesheet" href="https://fonts.googleapis.com/css2?family=Questrial&display=swap">
<style>
  :root{
    --blue:#0792cd;
    --blue-soft:#33a6d7;
    --sky:#85cae6;
    --mint:#86cfc6;
    --teal:#33b8a4;
    --ink-blue:#12608f;
    --ink:#111111;
    --white:#ffffff;
    --paper:#f4f6f7;
  }
  *{margin:0;padding:0;box-sizing:border-box}
  html,body{width:848px;height:1200px;overflow:hidden;background:var(--white)}
  body{font-family:"Questrial",sans-serif}
  .cover{position:relative;width:848px;height:1200px;overflow:hidden}
  .cover-art{position:absolute;inset:0;width:848px;height:1200px}
  .site-url{position:absolute;left:50px;top:50px;font-size:25px;color:var(--sky);letter-spacing:.5px}
  .edition{position:absolute;left:532px;top:92px;font-size:118px;line-height:1;color:var(--teal)}
  .edition sup{font-size:28px;position:relative;top:-62px;left:2px}
  .title{position:absolute;left:260px;top:202px;font-size:93px;line-height:92px;color:var(--ink-blue);font-weight:400}
  .place{position:absolute;left:265px;top:396px;font-size:31px;letter-spacing:24px;color:var(--teal)}
  .year{position:absolute;left:640px;top:378px;font-size:60px;color:var(--ink)}
  .date-badge{position:absolute;left:75px;top:596px;width:330px;text-align:center}
  .date-month{font-size:34px;color:var(--teal);line-height:1;margin-top:60px}
  .date-day{font-size:49px;color:var(--teal);line-height:1;margin-top:6px}
  .date-num{font-size:93px;color:var(--white);line-height:1;margin-top:14px}
  .date-time{font-size:41px;color:var(--white);line-height:1;margin-top:0}
  .venue{position:absolute;right:51px;top:930px;font-size:24px;color:var(--white)}
  .blurb{position:absolute;left:396px;top:980px;width:432px;font-size:13.6px;line-height:17px;color:var(--white)}
  .contact{position:absolute;left:76px;top:1050px;color:var(--white)}
  .contact-label{font-size:9px;letter-spacing:.3px}
  .contact-mail{font-size:15px}
  .sponsors{position:absolute;left:0;top:1088px;width:848px;height:112px;display:flex;align-items:center;justify-content:space-between;padding:0 36px;list-style:none}
  .sponsor{display:flex;align-items:center;gap:5px;font-size:12px;color:var(--ink-blue)}
  .sponsor-dot{width:8px;height:8px;border-radius:50%;background:var(--blue)}
</style>
</head>
<body>
<main class="cover">
  <svg class="cover-art" viewBox="0 0 1000 1414" preserveAspectRatio="none" aria-hidden="false">
    <defs>
      <linearGradient id="bgBlue" x1="0" y1="0" x2="0.3" y2="1">
        <stop offset="0" stop-color="#0792cd"/>
        <stop offset="0.3" stop-color="#85cae6"/>
        <stop offset="0.7" stop-color="#33a6d7"/>
        <stop offset="1" stop-color="#0792cd"/>
      </linearGradient>
      <linearGradient id="skyline" x1="0" y1="0" x2="0" y2="1">
        <stop offset="0" stop-color="#f4f6f7"/>
        <stop offset="0.2" stop-color="#dfe3e6"/>
        <stop offset="0.7" stop-color="#cfd5d9"/>
        <stop offset="1" stop-color="#e8ecef"/>
      </linearGradient>
      <linearGradient id="badge" x1="0" y1="0" x2="1" y2="1">
        <stop offset="0" stop-color="#0792cd"/>
        <stop offset="1" stop-color="#0a7cb3"/>
      </linearGradient>
      <clipPath id="leafClip">
        <path d="M430,108 C700,40 950,30 1000,30 L1000,430 C900,780 720,1030 440,1150 L0,1150 L0,700 C60,420 210,180 430,108 Z"/>
      </clipPath>
    </defs>
    <rect class="bg" width="1000" height="1414" fill="url(#bgBlue)"/>
    <path class="leaf" d="M430,108 C700,40 950,30 1000,30 L1000,430 C900,780 720,1030 440,1150 L0,1150 L0,700 C60,420 210,180 430,108 Z" fill="#f6f7f8"/>
    <g role="img" aria-label="Faded grey photograph of the Singapore waterfront skyline" clip-path="url(#leafClip)">
      <rect x="0" y="500" width="1000" height="650" fill="url(#skyline)"/>
    </g>
    <path class="swoosh-teal" d="M385,122 C210,215 70,380 0,560 L0,640 C70,420 220,230 385,122 Z" fill="#33b8a4"/>
    <path class="swoosh-blue" d="M415,112 C240,220 100,410 30,640 C110,420 250,240 415,112 Z" fill="#0792cd"/>
    <path class="swoosh-teal" d="M1000,410 C940,700 780,960 540,1120 C800,990 960,760 1000,560 Z" fill="#33b8a4"/>
    <path class="swoosh-blue" d="M990,470 C910,760 760,980 500,1140 C780,1010 930,780 990,470 Z" fill="#0a6fa8"/>
    <circle class="date-disc" cx="283" cy="898" r="195" fill="url(#badge)"/>
    <rect class="footer-band" x="0" y="1283" width="1000" height="131" fill="#ffffff"/>
  </svg>

  <p class="site-url">LumoraSummit.com</p>
  <p class="edition">3<sup>rd</sup></p>
  <h1 class="title">Lumora<br>Summit</h1>
  <p class="place">SINGAPORE</p>
  <p class="year">2018</p>

  <div class="date-badge">
    <p class="date-month">OCTOBER</p>
    <p class="date-day">SUNDAY</p>
    <p class="date-num">28</p>
    <p class="date-time">6:30pm</p>
  </div>

  <p class="venue">Local: Lorem ipsum</p>
  <p class="blurb">At vero eos et accusamus et iusto odio dignissimos ducimus qui blanditiis praesentium voluptatum deleniti atque corrupti quos dolores et quas molestias excepturi sint occaecati cupiditate non provident, similique sunt in culpa qui officia deserunt mollitia animi, id est laborum et dolorum fuga.</p>

  <div class="contact">
    <p class="contact-label">QUESTIONS? CONTACT</p>
    <p class="contact-mail">hello@lumorasummit.com</p>
  </div>

  <ul class="sponsors">
    <li class="sponsor"><span class="sponsor-dot"></span>Rivermoor</li>
    <li class="sponsor">Oakfield</li>
    <li class="sponsor">Fernhollow</li>
    <li class="sponsor">Keelbright</li>
    <li class="sponsor">Hopstead</li>
    <li class="sponsor">Northbank Club</li>
    <li class="sponsor">Trailwise</li>
    <li class="sponsor">Stillwater</li>
    <li class="sponsor">Canoro</li>
    <li class="sponsor">Tideline</li>
  </ul>
</main>
</body>
</html>
```